Amber Hollow Productions

I need a business card design for a new freelance film production company using or incorporating the logo:
I want the card to be creative, minimal, yet professional. Feel free to use a variety of different shapes and sizes/ textures for the card.

Industry/Entity Type

Film Production

```html
<!DOCTYPE html>
<html lang="en">
<head>
<meta charset="utf-8">
<title>Amber Hollow Productions – Business Card</title>
<link rel="stylesheet" href="https://fonts.googleapis.com/css2?family=Questrial&display=swap">
<style>
  :root {
    --stage: #e9e9ea;
    --brand-blue: #0a4592;
    --card-top: #e4e4e5;
    --card-bottom: #ffffff;
    --ink-light: #ffffff;
    --ink-grey: #7b7d80;
  }
  * { margin: 0; padding: 0; box-sizing: border-box; }
  html, body { width: 1200px; height: 900px; overflow: hidden; }
  body {
    background: var(--stage);
    font-family: "Questrial", "Century Gothic", sans-serif;
    position: relative;
  }
  .card {
    position: absolute;
    top: 302px;
    width: 513px;
    height: 295px;
    border-radius: 22px;
    overflow: hidden;
    background: linear-gradient(to bottom, var(--card-top), var(--card-bottom));
    box-shadow: 0 4px 10px rgba(0,0,0,0.25);
  }
  .card--front { left: 73px; }
  .card--back { left: 616px; }

  .brand {
    position: absolute;
    display: flex;
    align-items: center;
    color: var(--brand-blue);
    font-weight: 400;
  }
  .brand__square {
    flex: none;
    background: var(--brand-blue);
  }
  .brand__name { text-transform: uppercase; letter-spacing: 0.04em; line-height: 1.15; }

  .card--front .brand {
    left: 0; right: 0; top: 0; bottom: 0;
    justify-content: center;
    gap: 18px;
  }
  .card--front .brand__square { width: 26px; height: 26px; }
  .card--front .brand__name { font-size: 34px; }

  .back-panel { position: absolute; left: 0; top: 0; }
  .back-panel path { fill: var(--brand-blue); }

  .contact {
    position: absolute;
    left: 40px;
    top: 48px;
    color: var(--ink-light);
  }
  .contact__name { font-size: 20px; line-height: 24px; }
  .contact__role { font-size: 14px; line-height: 18px; margin-bottom: 30px; }
  .contact__list { list-style: none; font-size: 14px; }
  .contact__list li { display: flex; align-items: flex-start; line-height: 17px; }
  .contact__list svg { width: 10px; height: 10px; margin: 3px 8px 0 0; flex: none; fill: var(--ink-light); }
  .contact__gap { height: 28px; }

  .card--back .brand {
    left: 305px;
    width: 180px;
    top: 0; bottom: 0;
    gap: 10px;
  }
  .card--back .brand__square { width: 14px; height: 14px; }
  .card--back .brand__name { font-size: 19px; }
</style>
</head>
<body>

<section class="card card--front">
  <div class="brand">
    <span class="brand__square"></span>
    <span class="brand__name">Amber Hollow<br>Productions</span>
  </div>
</section>

<section class="card card--back">
  <svg class="back-panel" width="513" height="295" viewBox="0 0 513 295">
    <path d="M0 0 H241 C274 90 274 205 241 295 H0 Z"/>
  </svg>

  <div class="contact">
    <p class="contact__name">Nora Castellan</p>
    <p class="contact__role">managing director</p>
    <ul class="contact__list">
      <li><svg viewBox="0 0 10 10"><path d="M2.5 0 H7.5 V10 H2.5 Z M3.5 1 V8 H6.5 V1 Z"/></svg>212 640 18 27</li>
      <li><svg viewBox="0 0 10 10"><path d="M2.5 0 H7.5 V3 H10 V8 H8 V10 H2 V8 H0 V3 H2.5 Z M3 6.5 V9 H7 V6.5 Z"/></svg>212 640 18 28</li>
      <li><svg viewBox="0 0 10 10"><path d="M0 2 H10 V8 H0 Z M1 3 L5 5.6 L9 3 Z" fill-rule="evenodd"/></svg>hello@amberhollow.com</li>
      <li class="contact__gap"></li>
      <li><svg viewBox="0 0 10 10"><path d="M5 0 C7.2 0 8.5 1.6 8.5 3.5 C8.5 6 5 10 5 10 C5 10 1.5 6 1.5 3.5 C1.5 1.6 2.8 0 5 0 Z M5 2.2 A1.3 1.3 0 1 0 5 4.8 A1.3 1.3 0 1 0 5 2.2 Z" fill-rule="evenodd"/></svg><span>48 Larkmoor Lane, Eastvale<br>New York 10477</span></li>
      <li><svg viewBox="0 0 10 10"><path d="M5 0 A5 5 0 1 0 5 10 A5 5 0 1 0 5 0 Z M1 4.5 H9 V5.5 H1 Z M4.5 1 H5.5 V9 H4.5 Z" fill-rule="evenodd"/></svg>www.amberhollow.com</li>
    </ul>
  </div>

  <div class="brand">
    <span class="brand__square"></span>
    <span class="brand__name">Amber Hollow<br>Productions</span>
  </div>
</section>

</body>
</html>
```